Waterproofing Construction company needs letterhead

I need a letterhead design for a commercial waterproofing construction company. We would like to see designs that are contemporary, clean, sleek and use our logo. Our current design is dated. I would also like a cover page (see example) that goes with our letterhead. I would like for the footer to have our address, website, and phone number

Target Market(s)

Customers, potential customers.

Font styles to use
Sans Serif

Requirements
Must have
• logo, website, address, phone numbers, only our colors, tahoma font
• PMS: 295C PMS: 2995C
• CMYK: 100/84/36/39 CMYK: 80/12/1/0
• RGB: 16/44/82 RGB: 0/167/224
• HEX#: #102C52 HEX#: #00A7E0
• Black & White: 100% Black & White: 32%
• Gray Scale: 90% Gray Scale: 32%
Nice to have
• Our "icon" logo attached would be nice somewhere on the page.

```html
<!DOCTYPE html>
<html lang="en">
<head>
<meta charset="utf-8">
<title>Tidewall Letterhead</title>
<link rel="stylesheet" href="https://fonts.googleapis.com/css2?family=Questrial&family=PT+Sans:wght@400&display=swap">
<style>
  :root {
    --navy: #102C52;
    --sky: #00A7E0;
    --paper: #f3f3f4;
    --paper-edge: #ececee;
    --body-text: #5a5a5e;
    --greeting: #4a4a4e;
    --footer-text: #55555a;
    --signature-tone: #dde8f3;
  }
  * { margin: 0; padding: 0; box-sizing: border-box; }
  html, body { width: 850px; height: 1200px; overflow: hidden; background: #ffffff; }
  .letterhead {
    position: relative;
    width: 850px;
    height: 1200px;
    background: linear-gradient(160deg, #f8f8f9 0%, var(--paper) 55%, var(--paper-edge) 100%);
    font-family: "Questrial", "Century Gothic", sans-serif;
    overflow: hidden;
  }
  .side-band {
    position: absolute;
    left: 0; top: 0;
    width: 17px; height: 100%;
    background: var(--navy);
  }
  .brand {
    position: absolute;
    top: 88px; left: 0; width: 100%;
    text-align: center;
    color: var(--navy);
  }
  .brand-name {
    display: inline-flex;
    align-items: center;
    gap: 10px;
    font-size: 50px;
    line-height: 1;
    letter-spacing: 1px;
  }
  .brand-dot {
    width: 14px; height: 14px;
    background: var(--sky);
  }
  .brand-tagline {
    margin-top: 6px;
    font-size: 12.5px;
    letter-spacing: 0.3px;
  }
  .letter {
    position: absolute;
    left: 72px; top: 312px;
    width: 680px;
    color: var(--body-text);
  }
  .greeting {
    font-size: 21px;
    color: var(--greeting);
    margin-bottom: 30px;
  }
  .letter p {
    font-size: 11.6px;
    line-height: 17.5px;
    text-align: justify;
    margin-bottom: 17px;
  }
  .closing { margin-top: 30px; font-size: 11.6px; }
  .signature {
    display: block;
    margin-top: 22px;
    margin-left: -8px;
    width: 150px; height: 54px;
    border-radius: 4px;
    background: linear-gradient(90deg, var(--signature-tone), rgba(221,232,243,0.3));
  }
  .footer {
    position: absolute;
    left: 17px; right: 0; top: 1098px;
    text-align: center;
    font-family: "PT Sans", "Myriad Pro", sans-serif;
    font-size: 12px;
    line-height: 17px;
    color: var(--footer-text);
  }
  .contact-line {
    display: inline-flex; align-items: center; gap: 4px;
  }
  .contact-line svg { width: 12px; height: 12px; fill: var(--navy); }
  .contact-line .gap { margin-left: 2px; }
</style>
</head>
<body>
<main class="letterhead">
  <div class="side-band"></div>

  <header class="brand">
    <div class="brand-name"><span>TIDEWALL</span><span class="brand-dot"></span></div>
    <div class="brand-tagline">WATERPROOFING • RESTORATION</div>
  </header>

  <section class="letter">
    <h1 class="greeting" style="font-weight:400">Dear Mr. Carter,</h1>
    <p>Lorem ipsum dolor sit amet, consectetur adipiscing elit. Donec orci purus, luctus vitae dignissim eu, iaculis sed purus. Vivamus faucibus, ipsum nec aliquet viverra, leo mauris condimentum ligula, sit amet sagittis enim ligula quis arcu. Nam egestas tortor id nisi porttitor mattis. In tortor ante, ultricies in suscipit a, tempus non massa. Vivamus et auctor mi. Fusce vel massa nulla. Phasellus nec eros mauris, et scelerisque orci.</p>
    <p>Donec malesuada orci vitae nulla accumsan porta a id massa. Quisque accumsan iaculis magna sit amet fringilla. Maecenas consequat, magna eget tincidunt semper, odio nibh rutrum mi, id feugiat ante nisi eu risus. Vestibulum nunc orci, rhoncus a placerat in, ultricies in mi. Cras mattis varius eros, vel fringilla nisi suscipit eget. Quisque scelerisque sagittis nulla at porttitor.</p>
    <p>Sed id augue vitae urna euismod commodo aliquet a quam. Pellentesque arcu velit, cursus et malesuada ut, consequat et diam. Nullam erat sem, rhoncus id ullamcorper vitae, rhoncus et arcu. In ultricies ultricies nulla, ut rutrum nisi iaculis at. Donec eu magna a metus ornare faucibus. Fusce aliquet faucibus ultricies. Morbi semper, est id tincidunt gravida, sem arcu adipiscing lacus, ac bibendum nulla leo eu purus. Quisque nec diam sed risus consectetur a accumsan quis quis nibh. Vestibulum id purus lorem.</p>
    <p>It is a long established fact that a reader will be distracted by the readable content of a page when looking at its layout. The point of using Lorem Ipsum is that it has a more-or-less normal distribution of letters, as opposed to using 'Content here, content here', making it look like readable English. Many desktop publishing packages</p>
    <div class="closing">Sincerely,</div>
    <span class="signature" role="img" aria-label="Handwritten signature of Daniel Reyes"></span>
  </section>

  <footer class="footer">
    <div>PO Box 314, Cary, NC 27511</div>
    <div class="contact-line">
      <svg viewBox="0 0 24 24" aria-hidden="true"><path d="M6.6 10.8a15.1 15.1 0 0 0 6.6 6.6l2.2-2.2a1 1 0 0 1 1-.25 11.4 11.4 0 0 0 3.6.57 1 1 0 0 1 1 1V20a1 1 0 0 1-1 1A17 17 0 0 1 3 4a1 1 0 0 1 1-1h3.5a1 1 0 0 1 1 1c0 1.25.2 2.45.57 3.6a1 1 0 0 1-.25 1z"/></svg>
      <span>(877) 555-0162</span>
      <svg class="gap" viewBox="0 0 24 24" aria-hidden="true"><path d="M6 3h12v5H6zM3 9h18v8h-3v4H6v-4H3zm5 6v4h8v-4z"/></svg>
      <span>(919) 555-0187</span>
      <svg class="gap" viewBox="0 0 24 24" aria-hidden="true"><circle cx="12" cy="12" r="10"/></svg>
      <span>www.tidewallwp.com</span>
    </div>
    <div>North Carolina | South Carolina | Virginia</div>
  </footer>
</main>
</body>
</html>
```